Birchline Septic Solutions

Would like to see some single sided ones but would also like to see some double sided with one sided only being the logo. Owners name is Tom Halvick. Phone number is 555-214-0387
Services are pumping, inspections, installs, and repairs

Contact Information for Business Card

555-241-0387 Tom Halvick Alder Falls, WY

```html
<!DOCTYPE html>
<html lang="en">
<head>
<meta charset="utf-8">
<title>Birchline Septic Solutions – Business Cards</title>
<link rel="stylesheet" href="https://fonts.googleapis.com/css2?family=Barlow+Condensed:wght@600;700&display=swap">
<style>
  :root {
    --backdrop: #3b3c45;
    --card: #050505;
    --teal: #2bb3a8;
    --white: #f4f4f4;
  }
  * { margin: 0; padding: 0; box-sizing: border-box; }
  html, body {
    width: 1200px; height: 1200px; overflow: hidden;
    background: var(--backdrop);
    font-family: "Barlow Condensed", "Arial Narrow", sans-serif;
  }
  .card {
    position: absolute;
    width: 760px; height: 434px;
    background: var(--card);
    overflow: hidden;
  }
  .card--front { left: 220px; top: 130px; }
  .card--back  { left: 220px; top: 636px; }

  .wordmark {
    position: absolute; inset: 0;
    display: flex; align-items: center; justify-content: center; gap: 18px;
  }
  .wordmark__square {
    width: 30px; height: 30px; background: var(--teal);
  }
  .wordmark__name {
    color: var(--white);
    font-weight: 700;
    font-size: 50px;
    letter-spacing: 3px;
    text-transform: uppercase;
  }

  .contact {
    position: absolute; left: 0; right: 0; top: 58px;
    text-align: center; text-transform: uppercase;
    font-weight: 700;
  }
  .contact__name {
    color: var(--teal);
    font-size: 46px; line-height: 1;
    letter-spacing: 0.5px;
  }
  .contact__phone-row {
    display: flex; align-items: center; justify-content: center; gap: 22px;
    margin-top: 14px;
  }
  .contact__rule {
    width: 92px; height: 2px; background: var(--white);
  }
  .contact__phone {
    color: var(--white);
    font-size: 42px; line-height: 1;
    text-transform: none;
  }
  .services {
    margin-top: 34px;
    color: var(--white);
    font-size: 32px; line-height: 1.15;
    font-weight: 600;
  }
  .accent {
    position: absolute; left: 0; top: 0;
    width: 760px; height: 434px;
  }
</style>
</head>
<body>

  <section class="card card--front" aria-label="Card front">
    <div class="wordmark">
      <span class="wordmark__square"></span>
      <span class="wordmark__name">Birchline Septic Solutions</span>
    </div>
  </section>

  <section class="card card--back" aria-label="Card back">
    <div class="contact">
      <p class="contact__name">Tom Halvick Alder Falls, WY</p>
      <div class="contact__phone-row">
        <span class="contact__rule"></span>
        <span class="contact__phone">p.555-241-0387</span>
        <span class="contact__rule"></span>
      </div>
      <div class="services">
        <p>Services are</p>
        <p>Pumping | Inspections | Installs | Repairs</p>
      </div>
    </div>
    <svg class="accent" viewBox="0 0 760 434" aria-hidden="true">
      <polygon points="0,362 470,362 446,392 0,392" fill="var(--teal)"/>
      <polygon points="500,400 760,400 760,434 474,434" fill="var(--white)"/>
    </svg>
  </section>

</body>
</html>
```